Stationery using new logo for pharmacy and gift shop

We need a letterhead, business card, gift voucher and possibly compliments slip design for our pharmacy and gift shop using our new logo.
The letterhead would need to be produced in both colour (purple and green) and grayscale and the business card would preferably be one-sided, but can be two-sided if this works better with the information it needs to have on it.

We would like a simple and elegant design, but not so simple that it looks like we've done it ourselves on Word. Use of our colours would be great but the letterhead would need to look good if printed on our black and white laser printer. If this is not possible then an additional version for grayscale would be needed.

We would need to receive high quality files that we can work with easily, such as pdf's for the letterhead that we can print instantly or order online as it appears on screen and business cards in jpeg and pdf so we can upload to printing sites.
We would like the vouchers in denominations of £5 and £10 in A5 size in a printable format such as PDF so that we don't have to resize.

Letterhead is for use in correspondence and invoicing to patients, surgeries, traders, customers etc.

Our preferred font is Orkney

Letterhead Info
Address
47 Fenwick Rd.
Ashbeck
Westmere
CA17 4TW

Tel: (01632) 357148
Fax: (01632) 364057
Website: www.brackenfieldpharmacy.com
Email: patientcare@brackenfieldpharmacy.com

Business Card Info.
As above but email address is: rtkdenholm@postbox-mail.co.uk

Voucher Info.
Small print to state that any change will be paid as a credit note.
Space for a staff member to sign, date and stamp voucher

I have quite a few logo files so please ask if you need more uploaded. Or if you need more information to improve the design then please contact me.

Target Market(s)

Both retail customers and professional colleagues

Industry/Entity Type

Pharmacy

Font styles to use
Other font styles liked:
• orkney

Colors
ffffff
9bcb3c
6b449b

Requirements
Must have
• Must be clear and legible with a professional feel. Must use the logo well and all aspects of the designs should work well together.
• Final files MUST be easy to use for non-computer specialists. I need staff to be able to pull up a letterhead template easily if they are writing a letter or raising an invoice. The business card must be in a format ready to be sent to print.
Nice to have
• Letterhead available in a word processor program like word so that letters can be sent by email as well as print or print and scan.

```html
<!DOCTYPE html>
<html lang="en">
<head>
<meta charset="utf-8">
<title>Brackenfield Pharmacy – Stationery Set</title>
<link rel="stylesheet" href="https://fonts.googleapis.com/css2?family=Questrial&family=Barlow+Condensed:wght@700&family=Montserrat:wght@600;800&display=swap">
<style>
  :root {
    --purple: #6b449b;
    --green: #9bcb3c;
    --white: #ffffff;
    --ink: #333333;
    --backdrop: #e9e8e4;
  }
  * { box-sizing: border-box; margin: 0; padding: 0; }
  html, body { width: 1200px; height: 675px; overflow: hidden; }
  body {
    position: relative;
    background: var(--backdrop);
    font-family: "Questrial", "Helvetica Neue", Arial, sans-serif;
    color: var(--ink);
  }
  .sheet {
    position: absolute;
    background: var(--white);
    overflow: hidden;
    box-shadow: 0 1px 4px rgba(0,0,0,.18);
  }

  /* brand name block */
  .mark { position: absolute; text-align: center; }
  .mark-square { display: block; margin: 0 auto; background: var(--purple); }
  .mark-name {
    display: block;
    color: var(--purple);
    font-family: "Questrial", Arial, sans-serif;
    letter-spacing: .03em;
    line-height: 1.1;
    white-space: nowrap;
    text-transform: uppercase;
  }

  /* bands */
  .rule { position: absolute; left: 0; right: 0; background: var(--purple); }
  .band {
    position: absolute; left: 0; right: 0; bottom: 0;
    background: var(--green);
    color: var(--white);
    display: flex; flex-direction: column; align-items: center; justify-content: center;
    text-align: center;
  }
  .url { letter-spacing: .12em; }
  .icon { width: 1em; height: 1em; vertical-align: -0.12em; fill: currentColor; }
  .contact-line { white-space: nowrap; }
  .contact-line span { margin: 0 .3em; }

  /* business card front */
  .card-front { left: 254px; top: 49px; width: 162px; height: 104px; }
  .card-front .mark { left: 2px; top: 25px; width: 90px; }
  .card-front .mark-square { width: 22px; height: 22px; margin-bottom: 4px; }
  .card-front .mark-name { font-size: 7px; }
  .card-details { position: absolute; left: 91px; top: 24px; font-size: 4.3px; line-height: 1.5; color: var(--ink); }
  .card-holder { font-family: "Montserrat", sans-serif; font-weight: 600; color: var(--purple); font-size: 5.4px; margin-bottom: 3px; }
  .card-front .rule { top: 89px; height: 1.5px; }
  .card-front .band { height: 9px; font-size: 4.4px; }

  /* business card back */
  .card-back { left: 436px; top: 49px; width: 162px; height: 104px; background: var(--purple); }
  .card-back .mark { left: 0; right: 0; top: 27px; }
  .card-back .mark-square { width: 30px; height: 30px; background: var(--white); margin-bottom: 6px; }
  .card-back .mark-name { color: var(--white); font-size: 9px; }

  /* letterhead */
  .letterhead { left: 618px; top: 48px; width: 400px; height: 566px; }
  .letterhead .mark { left: 0; right: 0; top: 32px; }
  .letterhead .mark-square { width: 46px; height: 46px; margin-bottom: 8px; }
  .letterhead .mark-name { font-size: 16px; line-height: 1; }
  .letter-body { position: absolute; left: 43px; top: 138px; width: 315px; font-size: 5.9px; line-height: 1.4; color: var(--ink); }
  .letter-date { margin-bottom: 17px; }
  .letter-greeting { margin-bottom: 30px; }
  .letter-body p { margin-bottom: 9px; }
  .letter-signoff { margin-top: 12px; }
  .letter-footer { position: absolute; left: 0; right: 0; top: 503px; text-align: center; font-size: 5.9px; line-height: 1.6; }
  .letterhead .rule { top: 540px; height: 4px; }
  .letterhead .band { height: 20px; }

  /* envelope */
  .envelope { left: 85px; top: 164px; width: 418px; height: 208px; }
  .envelope .mark { left: 14px; top: 22px; width: 140px; }
  .envelope .mark-square { width: 38px; height: 38px; margin-bottom: 6px; }
  .envelope .mark-name { font-size: 12px; }
  .envelope-address { position: absolute; left: 23px; top: 97px; font-size: 6.2px; color: #222; }
  .envelope .rule { top: 180px; height: 4px; }
  .envelope .band { height: 23px; font-size: 11px; }

  /* compliments slip */
  .compliments { left: 450px; top: 290px; width: 329px; height: 157px; box-shadow: 0 2px 8px rgba(0,0,0,.25); }
  .compliments .mark { left: 10px; top: 12px; width: 120px; }
  .compliments .mark-square { width: 34px; height: 34px; margin-bottom: 6px; }
  .compliments .mark-name { font-size: 11px; }
  .compliments-title { position: absolute; right: 14px; top: 20px; font-family: "Montserrat", sans-serif; font-weight: 600; color: var(--purple); font-size: 13px; }
  .compliments .rule { top: 126px; height: 3px; }
  .compliments .band { height: 25px; font-size: 4.6px; line-height: 1.8; }

  /* gift vouchers */
  .voucher { width: 294px; height: 210px; }
  .voucher-five { left: 96px; top: 386px; }
  .voucher-ten { left: 350px; top: 455px; box-shadow: 0 2px 8px rgba(0,0,0,.25); }
  .voucher .mark { left: 0; width: 166px; top: 22px; }
  .voucher .mark-square { width: 36px; height: 36px; margin-bottom: 5px; }
  .voucher .mark-name { font-size: 12.5px; }
  .voucher-title {
    position: absolute; left: 0; width: 166px; top: 94px; text-align: center;
    font-family: "Barlow Condensed", sans-serif; font-weight: 700; font-size: 25px; color: var(--purple); letter-spacing: .01em;
  }
  .voucher-note { position: absolute; left: 0; width: 166px; top: 123px; text-align: center; font-size: 6px; color: var(--green); }
  .voucher-sign { position: absolute; top: 154px; font-size: 5.6px; color: var(--purple); text-align: center; border-top: .6px solid #b9a8d2; padding-top: 2px; }
  .voucher-sign.signature { left: 22px; width: 80px; }
  .voucher-sign.date-stamp { left: 188px; width: 80px; }
  .voucher .rule { top: 167px; height: 8px; }
  .voucher .band { height: 29px; font-size: 11.4px; }
  .voucher-banner { position: absolute; left: 168px; top: 0; width: 108px; height: 138px; }
  .voucher-value {
    position: absolute; left: 168px; width: 108px; top: 36px; text-align: center;
    font-family: "Montserrat", sans-serif; font-weight: 800; font-size: 50px; color: var(--white); letter-spacing: -.02em; line-height: 1;
  }
</style>
</head>
<body>

<svg width="0" height="0" style="position:absolute" aria-hidden="true">
  <symbol id="i-phone" viewBox="0 0 16 16"><path d="M3.6 1.5l2.3 2.8-1.4 1.6c.9 2 2.5 3.6 4.6 4.6l1.6-1.4 2.8 2.3-1.4 2.1C7 13.2 2.8 9 1.5 3z"/></symbol>
  <symbol id="i-fax" viewBox="0 0 16 16"><path d="M4 1h8v4H4zM2 6h12v6h-2v3H4v-3H2zm3 4v4h6v-4z"/></symbol>
  <symbol id="i-mail" viewBox="0 0 16 16"><path d="M1 3h14v10H1zm1.5 1.3V5l5.5 4 5.5-4v-.7z"/></symbol>
  <symbol id="i-web" viewBox="0 0 16 16"><path d="M8 1a7 7 0 100 14A7 7 0 008 1zm0 1.6a5.4 5.4 0 110 10.8A5.4 5.4 0 018 2.6zM2.8 7.3h10.4v1.4H2.8zM7.3 2.5h1.4v11H7.3z"/></symbol>
</svg>

<!-- Business card, front -->
<div class="sheet card-front">
  <div class="mark"><span class="mark-square"></span><span class="mark-name">Brackenfield<br>Pharmacy</span></div>
  <div class="card-details">
    <div class="card-holder">First Name Last Name</div>
    <div>47 Fenwick Rd. Ashbeck</div>
    <div>Westmere CA17 4TW</div>
    <div style="margin-top:2px"><svg class="icon"><use href="#i-phone"/></svg> (01632) 357148</div>
    <div><svg class="icon"><use href="#i-fax"/></svg> (01632) 364057</div>
    <div><svg class="icon"><use href="#i-mail"/></svg> rtkdenholm@postbox-mail.co.uk</div>
  </div>
  <div class="rule"></div>
  <div class="band"><span class="url">www.brackenfieldpharmacy.com</span></div>
</div>

<!-- Business card, back -->
<div class="sheet card-back">
  <div class="mark"><span class="mark-square"></span><span class="mark-name">Brackenfield<br>Pharmacy</span></div>
</div>

<!-- Letterhead -->
<div class="sheet letterhead">
  <div class="mark"><span class="mark-square"></span><span class="mark-name">Brackenfield<br>Pharmacy</span></div>
  <div class="letter-body">
    <div class="letter-date">December 27, 2017</div>
    <div class="letter-greeting">Dear Recipients :</div>
    <p>Lorem ipsum dolor sit amet, consectetur adipisicing elit, sed do eiusmod tempor incididunt ut labore et dolore magna aliquas Ut enim ad minim veniam, quis nostrud exercitation ullamco laboris nisi ut aliquip ex ea commodo consequat. Duis aute lore irure dolor in reprehenderit in voluptate velit esse cillum dolore eu fugiat nulla pariatur. Excepteur sint occaecat cupidatat non proident, sunt in culpa qui officia deserunt mollit anim id est laborum. Sed ut perspiciatis unde omnis iste natus error sit voluptatem accusantium doloremque laudantium, lorem ipsum dolor sit amet dolo consectetur adipisicing elit, sed do labore dolore magna aliqua.</p>
    <p>Lorem ipsum dolor sit amet, consectetur adipisicing elit, sed do eiusmod tempor incididunt ut labore et dolore magna aliqua. Ut enim ad minim veniam, quis nostrud exercitation ullamco laboris nisi ut aliquip ex ea commodo consequat. Duis aute irure dolor in reprehenderit in voluptate velit esse cillum dolore eu fugiat nulla pariatur. Excepteur sint occaecat non proident, sunt in culpa qui officia deserunt mollit anim id est laborum. Sed ut perspiciatis unde omnis iste sit aspernatur aut odit aut sed do eiusmod tempor incididunt ut labore.</p>
    <p>Lorem ipsum dolor sit amet, consectetur adipisicing elit, sed do eiusmod tempor incididunt ut labore et dolore magna aliqua. Ut enim ad minim veniam, quis nostrud exercitation ullamco laboris nisi ut aliquip ex ea commodo consequat. Duis aute irure dolor in reprehenderit in voluptate velit esse cillum dolore eu fugiat nulla pariatur. Excepteur sint occaecat non proident, sunt in culpa qui officia deserunt mollit anim id est laborum.</p>
    <p>Duis aute irure dolor in reprehenderit in voluptate velit esse cillum dolore eu fugiat nulla pariatur. Excepteur sint occaecat cupidatat non proident, sunt in culpa qui officia deserunt mollit anim.</p>
    <div class="letter-signoff">Thank You</div>
  </div>
  <div class="letter-footer">
    <div>47 Fenwick Rd. Ashbeck Westmere CA17 4TW</div>
    <div class="contact-line">
      <span><svg class="icon"><use href="#i-phone"/></svg> (01632) 357148</span>
      <span><svg class="icon"><use href="#i-fax"/></svg> (01632) 364057</span>
      <span><svg class="icon"><use href="#i-mail"/></svg> patientcare@brackenfieldpharmacy.com</span>
      <span><svg class="icon"><use href="#i-web"/></svg> www.brackenfieldpharmacy.com</span>
    </div>
  </div>
  <div class="rule"></div>
  <div class="band"></div>
</div>

<!-- Envelope -->
<div class="sheet envelope">
  <div class="mark"><span class="mark-square"></span><span class="mark-name">Brackenfield<br>Pharmacy</span></div>
  <div class="envelope-address">47 Fenwick Rd. Ashbeck Westmere CA17 4TW</div>
  <div class="rule"></div>
  <div class="band"><span class="url">www.brackenfieldpharmacy.com</span></div>
</div>

<!-- Compliments slip -->
<div class="sheet compliments">
  <div class="mark"><span class="mark-square"></span><span class="mark-name">Brackenfield<br>Pharmacy</span></div>
  <div class="compliments-title">With Compliments</div>
  <div class="rule"></div>
  <div class="band">
    <div>47 Fenwick Rd. Ashbeck Westmere CA17 4TW</div>
    <div class="contact-line">
      <span><svg class="icon"><use href="#i-phone"/></svg> (01632) 357148</span>
      <span><svg class="icon"><use href="#i-fax"/></svg> (01632) 364057</span>
      <span><svg class="icon"><use href="#i-mail"/></svg> patientcare@brackenfieldpharmacy.com</span>
      <span><svg class="icon"><use href="#i-web"/></svg> www.brackenfieldpharmacy.com</span>
    </div>
  </div>
</div>

<!-- £5 voucher -->
<div class="sheet voucher voucher-five">
  <svg class="voucher-banner" viewBox="0 0 108 138" aria-hidden="true">
    <polygon points="0,0 108,0 108,138 54,118 0,138" fill="#6b449b"/>
    <polyline points="6,0 6,126 54,108 102,126 102,0" fill="none" stroke="#fff" stroke-width=".7" stroke-dasharray="3 2"/>
  </svg>
  <div class="voucher-value">£5</div>
  <div class="mark"><span class="mark-square"></span><span class="mark-name">Brackenfield<br>Pharmacy</span></div>
  <div class="voucher-title">GIFT VOUCHER</div>
  <div class="voucher-note">*Any change will be paid as a credit note.</div>
  <div class="voucher-sign signature">signature</div>
  <div class="voucher-sign date-stamp">Date and Stamp</div>
  <div class="rule"></div>
  <div class="band"><span class="url">www.brackenfieldpharmacy.com</span></div>
</div>

<!-- £10 voucher -->
<div class="sheet voucher voucher-ten">
  <svg class="voucher-banner" viewBox="0 0 108 138" aria-hidden="true">
    <polygon points="0,0 108,0 108,138 54,118 0,138" fill="#6b449b"/>
    <polyline points="6,0 6,126 54,108 102,126 102,0" fill="none" stroke="#fff" stroke-width=".7" stroke-dasharray="3 2"/>
  </svg>
  <div class="voucher-value">£10</div>
  <div class="mark"><span class="mark-square"></span><span class="mark-name">Brackenfield<br>Pharmacy</span></div>
  <div class="voucher-title">GIFT VOUCHER</div>
  <div class="voucher-note">*Any change will be paid as a credit note.</div>
  <div class="voucher-sign signature">signature</div>
  <div class="voucher-sign date-stamp">Date and Stamp</div>
  <div class="rule"></div>
  <div class="band"><span class="url">www.brackenfieldpharmacy.com</span></div>
</div>

</body>
</html>
```